PACKAGING AND LABEL DESIGN FOR LUXURY WHISKY BRAND

We need a label and packaging design for a new luxury whisky brand based in Singapore called Morvane. We need a label design and a suggested packaging design in a box/bag or wrap form. For the bottle it is fixed, so we would like suggestions to make the bottle like a piece of art. Please refer to Harlow whisky, Kelpa Rum, PLR and Vireo coffee for the inspiration and styles we like. For the words 1746 and Oat Whisky please make original fonts or artwork. We would like it to be in Serif font but we are open to suggestions
The bottle is as attached with the following dimensions
Height :159mm
Diammeter:84mm
Outter Diameter of mouth:39mm

We develop the world's first soy wines and spirits. Our new product is a soy based whisky that pays tribute to tradition and culture in Singapore while showcasing our nation's innovative and courageous spirit, moving from a swamp to a first world nation.

Please read the brand guidelines for deeper understanding

Target Market(s)

Global travellers coming to Singapore. Adventurous, innovators and independent self made pride.

Industry/Entity Type

Alcohol beverages

Requirements
Must have
• Original label design a box/packaging design, logo of morvane, logo of 1746, fonts and art of the labels
Nice to have
• Original artwork for 1746 and Oat Whisky. Batik prints, gold, soy beans/flowers, Singapore elements.
Should not have
• No copied work.

```html
<!DOCTYPE html>
<html lang="en">
<head>
<meta charset="utf-8">
<title>Morvane 1746 Oat Whiskey – Box Front</title>
<link rel="stylesheet" href="https://fonts.googleapis.com/css2?family=Montserrat:wght@500&family=Playfair+Display:wght@700&family=Staatliches&family=Cinzel:wght@700&display=swap">
<style>
  :root {
    --paper: #ffffff;
    --panel: #0b0b0b;
    --panel-soft: #1a1a1a;
    --gold: #d3a43a;
    --gold-light: #f2d27a;
    --gold-deep: #8a6418;
    --ink-white: #f6f4ee;
  }
  html, body {
    margin: 0;
    padding: 0;
    width: 1200px;
    height: 1199px;
    overflow: hidden;
    background: var(--paper);
  }
  .artboard { display: block; width: 1200px; height: 1199px; }
  .brand-name {
    font-family: "Montserrat", sans-serif;
    font-weight: 500;
    fill: var(--gold);
  }
  .origin-tag {
    font-family: "Cinzel", serif;
    font-weight: 700;
    fill: var(--gold-light);
  }
  .vintage-mark {
    font-family: "Playfair Display", serif;
    font-weight: 700;
    fill: var(--ink-white);
  }
  .spec-text, .product-name {
    font-family: "Staatliches", sans-serif;
    fill: var(--ink-white);
  }
</style>
</head>
<body>
<svg class="artboard" viewBox="0 0 1200 1199" xmlns="http://www.w3.org/2000/svg">
  <defs>
    <linearGradient id="goldSheen" x1="0" y1="0" x2="1" y2="1">
      <stop offset="0" stop-color="#f2d27a"/>
      <stop offset="0.5" stop-color="#c8952c"/>
      <stop offset="1" stop-color="#8a6418"/>
    </linearGradient>
    <radialGradient id="panelGlow" cx="0.5" cy="0.45" r="0.7">
      <stop offset="0" stop-color="#1d1d1d"/>
      <stop offset="1" stop-color="#070707"/>
    </radialGradient>
    <path id="productArc" d="M505 776 Q600 830 695 776"/>
  </defs>

  <!-- box front panel -->
  <g class="box-front">
    <rect x="360" y="220" width="480" height="760" fill="url(#panelGlow)"
          role="img" aria-label="Black panel with a faint batik floral print"/>
    <line x1="360" y1="262" x2="840" y2="262" stroke="var(--gold)" stroke-width="3"/>
    <line x1="360" y1="938" x2="840" y2="938" stroke="var(--gold)" stroke-width="3"/>
  </g>

  <!-- label -->
  <g class="label">
    <path class="label-crest-top" d="M500 350 Q600 270 700 350 Z" fill="url(#goldSheen)" opacity="0.85"
          role="img" aria-label="Gold filigree crest ornament"/>
    <path class="label-crest-bottom" d="M500 850 Q600 930 700 850 Z" fill="url(#goldSheen)" opacity="0.85"
          role="img" aria-label="Gold filigree crest ornament"/>
    <rect class="label-corners" x="430" y="345" width="340" height="510" rx="24" fill="url(#goldSheen)" opacity="0.55"
          role="img" aria-label="Gold engraved corner ornaments"/>

    <rect class="label-field" x="452" y="358" width="296" height="484" rx="148" fill="var(--panel)"
          role="img" aria-label="Dark batik floral pattern behind the label text"/>
    <rect x="452" y="358" width="296" height="484" rx="148" fill="none" stroke="var(--gold)" stroke-width="5"/>
    <rect x="462" y="368" width="276" height="464" rx="138" fill="none" stroke="var(--ink-white)" stroke-width="1.5" stroke-dasharray="4 3"/>
    <rect x="470" y="376" width="260" height="448" rx="130" fill="none" stroke="var(--gold)" stroke-width="2"/>

    <!-- origin band -->
    <rect x="530" y="412" width="140" height="20" fill="var(--panel-soft)" stroke="var(--gold)" stroke-width="1.5"/>
    <text class="origin-tag" x="600" y="427" font-size="11" text-anchor="middle" letter-spacing="1">FROM SINGAPORE</text>

    <!-- brand mark -->
    <circle cx="600" cy="525" r="66" fill="none" stroke="var(--gold)" stroke-width="6"/>
    <text class="brand-name" x="602" y="658" font-size="36" text-anchor="middle" letter-spacing="5">MORVANE</text>

    <!-- vintage line -->
    <path class="vintage-crest" d="M560 702 Q600 684 640 702 Z" fill="url(#goldSheen)"
          role="img" aria-label="Small gold scroll ornament"/>
    <text class="spec-text" x="532" y="750" font-size="16" text-anchor="end">70cl e</text>
    <text class="vintage-mark" x="600" y="758" font-size="54" text-anchor="middle">1746</text>
    <text class="spec-text" x="666" y="750" font-size="16">40% Vol</text>

    <text class="product-name" font-size="28" letter-spacing="1">
      <textPath href="#productArc" startOffset="50%" text-anchor="middle">OAT WHISKEY</textPath>
    </text>
  </g>
</svg>
</body>
</html>
```